Fruity, Italy, Healthy Foods for thoughts.

We need a sign board design of a new Restaurant. Its name “Velmoranto Restaurant” and Arabic name “مطعم بلموراتو”. Although both names have to be appeared in signage in front of the shop but its ok you cannot do the Arabic one and make the design in English. Its Concept is; Fruits & Italian foods (means: fresh Juices, fruit salads, Pasta, Pizza and Veg. Salads), I've attached a typical design with actual measurements for your reference. I appreciate your creativity on the design as it will be applicable in future branches.
Updates

Project Deadline Extended
Reason: I have received only few designers (3 to 4) and only one having little acceptability but that no I want, and I have committed my payment I was expected more than 50 designers according to your message but unfortunately it's not happening please for you assistance.

Target Market(s)

All level of audience

Industry/Entity Type

Shop

Requirements
Must have
• Juicy fruity
Nice to have
• Juices fruits pasta pizza

```html
<!DOCTYPE html>
<html lang="en">
<head>
<meta charset="utf-8">
<title>Velmoranto Restaurant – Shop Sign</title>
<link rel="stylesheet" href="https://fonts.googleapis.com/css2?family=Fredoka:wght@700&family=Lalezar&display=swap">
<style>
  :root {
    --sign-white: #ffffff;
    --sign-orange: #f7931e;
    --sign-orange-light: #fcb233;
    --sign-red: rgba(232, 52, 22, .75);
    --sign-red-soft: rgba(232, 52, 22, .45);
    --sign-red-deep: #c9151a;
    --sign-outline: #dc2318;
    --splash-white: #f4fbff;
    --splash-blue: #a9d8ee;
    --splash-mid: #5fa9cf;
    --fruit-green: rgba(120, 170, 40, .55);
    --fruit-red: rgba(220, 40, 40, .5);
    --fruit-yellow: rgba(250, 200, 40, .6);
  }

  * { margin: 0; padding: 0; box-sizing: border-box; }

  html, body {
    width: 1200px;
    height: 272px;
    overflow: hidden;
    background: var(--sign-white);
  }

  .signboard {
    position: relative;
    width: 1200px;
    height: 272px;
  }

  .sign-band,
  .emblem {
    background:
      radial-gradient(ellipse 60px 30px at 6% 15%, var(--sign-red), transparent 70%),
      radial-gradient(ellipse 90px 40px at 14% 88%, var(--sign-red), transparent 70%),
      radial-gradient(ellipse 50px 25px at 24% 40%, var(--sign-red-soft), transparent 70%),
      radial-gradient(ellipse 110px 35px at 33% 12%, var(--sign-red), transparent 70%),
      radial-gradient(ellipse 70px 40px at 38% 78%, var(--sign-red), transparent 70%),
      radial-gradient(ellipse 60px 30px at 47% 30%, var(--sign-red-soft), transparent 70%),
      radial-gradient(ellipse 80px 30px at 56% 90%, var(--sign-red), transparent 70%),
      radial-gradient(ellipse 100px 40px at 64% 20%, var(--sign-red), transparent 70%),
      radial-gradient(ellipse 60px 35px at 71% 60%, var(--sign-red-soft), transparent 70%),
      radial-gradient(ellipse 90px 35px at 79% 12%, var(--sign-red), transparent 70%),
      radial-gradient(ellipse 110px 45px at 86% 85%, var(--sign-red), transparent 70%),
      radial-gradient(ellipse 60px 30px at 95% 35%, var(--sign-red), transparent 70%),
      radial-gradient(ellipse 40px 20px at 19% 62%, var(--sign-red-soft), transparent 70%),
      radial-gradient(ellipse 40px 20px at 91% 55%, var(--sign-red-soft), transparent 70%),
      linear-gradient(90deg, var(--sign-orange), var(--sign-orange-light) 30%, var(--sign-orange) 55%, var(--sign-orange-light) 80%, var(--sign-orange));
  }

  .sign-band {
    position: absolute;
    left: 15px;
    top: 70px;
    width: 1172px;
    height: 138px;
  }

  .emblem {
    position: absolute;
    left: 482px;
    top: 5px;
    width: 260px;
    height: 260px;
    border-radius: 50%;
  }

  .emblem-splash {
    position: absolute;
    left: 22px;
    top: 22px;
    width: 216px;
    height: 216px;
    border-radius: 50%;
    background:
      radial-gradient(circle at 30% 30%, var(--fruit-green), transparent 18%),
      radial-gradient(circle at 68% 28%, var(--fruit-red), transparent 15%),
      radial-gradient(circle at 72% 65%, var(--fruit-yellow), transparent 16%),
      radial-gradient(circle at 35% 75%, var(--fruit-green), transparent 15%),
      radial-gradient(circle at 55% 88%, rgba(245, 140, 30, .6), transparent 14%),
      radial-gradient(circle at 50% 50%, var(--splash-white) 0%, var(--splash-blue) 40%, var(--splash-mid) 65%, rgba(95, 169, 207, .2) 88%, transparent 100%);
  }

  .brand-latin {
    position: absolute;
    left: 28px;
    top: 92px;
    width: 440px;
    text-align: center;
    font-family: "Fredoka", sans-serif;
    font-weight: 700;
    color: var(--sign-white);
    -webkit-text-stroke: 5px var(--sign-outline);
    paint-order: stroke fill;
    text-shadow: 3px 3px 0 var(--sign-red-deep);
    line-height: 1;
  }

  .brand-latin .name {
    display: block;
    font-size: 62px;
    letter-spacing: 0;
  }

  .brand-latin .descriptor {
    display: block;
    margin-top: 0;
    font-size: 26px;
    letter-spacing: 1px;
    -webkit-text-stroke: 4px var(--sign-outline);
  }

  .brand-arabic {
    position: absolute;
    left: 745px;
    top: 72px;
    width: 435px;
    direction: rtl;
    text-align: center;
    font-family: "Lalezar", sans-serif;
    color: var(--sign-white);
    -webkit-text-stroke: 5px var(--sign-outline);
    paint-order: stroke fill;
    text-shadow: 3px 3px 0 var(--sign-red-deep);
    line-height: 1;
  }

  .brand-arabic .descriptor {
    display: block;
    font-size: 44px;
    padding-right: 140px;
    text-align: right;
  }

  .brand-arabic .name {
    display: block;
    font-size: 104px;
    margin-top: -34px;
  }
</style>
</head>
<body>
  <div class="signboard">
    <div class="sign-band"></div>

    <div class="emblem">
      <div class="emblem-splash" role="img" aria-label="Water splash swirling with fresh fruit: kiwi, orange, strawberry, pineapple, lime and mint leaves"></div>
    </div>

    <div class="brand-latin">
      <span class="name">VELMORANTO</span>
      <span class="descriptor">RESTAURANT</span>
    </div>

    <div class="brand-arabic" lang="ar">
      <span class="descriptor">مطعم</span>
      <span class="name">بلموراتو</span>
    </div>
  </div>
</body>
</html>
```